The tide parlor saltwater aquarium store business card

Looking for a serious business card for a saltwater fish and coral store. I want this thing to blow people's minds when they see it. I would like the card to look very professional but I also want people to know what the tide parlor is just by seeing the card. Iam pretty open to anything as long as it's one of a kind.

Industry/Entity Type

Business

Contact Information for Business Card

18635 Walden highway Brackton pa 15872. Thetideparlor.example. Customerservice@thetideparlor.example. 7245550148

Requirements
Should not have
• Please no child like fish designs

```html
<!DOCTYPE html>
<html lang="en">
<head>
<meta charset="utf-8">
<title>The Tide Parlor – Business Card</title>
<link rel="stylesheet" href="https://fonts.googleapis.com/css2?family=Open+Sans:wght@400;700&display=swap">
<style>
  :root {
    --backdrop: #1f1f21;
    --card: #ffffff;
    --wave-deep: #1b8fd5;
    --wave-mid: #3aa6e3;
    --wave-light: #8ccdf1;
    --wave-pale: #bfe3f7;
    --ink: #333a40;
    --ink-strong: #1e2428;
    --brand: #1b8fd5;
    --on-wave: #ffffff;
  }
  * { box-sizing: border-box; margin: 0; padding: 0; }
  html, body {
    width: 1200px; height: 1000px; overflow: hidden;
    background: var(--backdrop);
    font-family: "Open Sans", Arial, sans-serif;
  }
  .stage { position: relative; width: 1200px; height: 1000px; }

  .card {
    position: absolute;
    width: 520px; height: 300px;
    background: var(--card);
    border-radius: 52px 8px 52px 8px;
    overflow: hidden;
    box-shadow: 0 18px 40px rgba(0,0,0,.45);
  }
  .card-back  { left: 70px;  top: 520px; }
  .card-front { left: 610px; top: 180px; }

  .waves { position: absolute; inset: 0; width: 100%; height: 100%; }

  /* contact side */
  .contact-name {
    position: absolute; left: 44px; top: 34px;
    color: var(--on-wave); font-weight: 700; font-size: 21px;
  }
  .contact-email {
    position: absolute; left: 44px; top: 66px;
    color: var(--on-wave); font-size: 13px; letter-spacing: .2px;
  }
  .contact-details { position: absolute; left: 44px; top: 200px; color: var(--ink); }
  .phone-line { display: flex; align-items: center; gap: 8px; }
  .phone-icon { width: 16px; height: 16px; }
  .phone-number { font-weight: 700; font-size: 13px; color: var(--ink-strong); letter-spacing: .5px; }
  .address { margin-top: 6px; font-size: 12.5px; }

  /* brand side */
  .brand-lockup {
    position: absolute; left: 46px; top: 64px;
    display: flex; align-items: center; gap: 14px;
  }
  .brand-dot { width: 38px; height: 38px; border-radius: 50%; background: var(--brand); }
  .brand-name { color: var(--brand); font-weight: 700; font-size: 34px; line-height: 1; }
  .website {
    position: absolute; right: 44px; bottom: 40px;
    color: var(--on-wave); font-size: 15px; letter-spacing: .3px;
  }
</style>
</head>
<body>
<main class="stage">

  <section class="card card-back" aria-label="Contact side of the business card">
    <svg class="waves" viewBox="0 0 520 300" preserveAspectRatio="none" aria-hidden="true">
      <path fill="var(--wave-pale)" d="M0,0 H230 C280,10 290,80 350,100 C410,118 470,118 520,122 V222 C460,214 400,212 340,206 C270,198 240,150 180,140 C110,128 50,150 0,158 Z"/>
      <path fill="var(--wave-light)" opacity=".85" d="M0,0 H210 C265,8 275,78 335,96 C400,114 465,116 520,124 V208 C455,200 395,196 335,190 C265,184 235,130 170,120 C105,110 50,132 0,140 Z"/>
      <path fill="var(--wave-mid)" d="M0,0 H195 C250,10 262,80 322,96 C390,112 460,118 520,128 V190 C450,182 390,180 330,174 C260,168 230,116 168,104 C108,92 50,112 0,124 Z"/>
      <path fill="var(--wave-deep)" d="M0,0 H180 C235,12 248,76 308,92 C370,108 440,112 520,118 V160 C445,156 385,156 325,150 C258,144 225,102 165,92 C108,82 50,96 0,104 Z"/>
    </svg>
    <h2 class="contact-name">The Tide Parlor</h2>
    <p class="contact-email">Customerservice@thetideparlor.example</p>
    <div class="contact-details">
      <div class="phone-line">
        <svg class="phone-icon" viewBox="0 0 16 16" aria-hidden="true">
          <rect width="16" height="16" rx="2" fill="var(--wave-deep)"/>
          <path fill="#fff" d="M4.5 3.5 L6.3 3.5 L7 6 L5.9 6.9 C6.5 8.2 7.6 9.3 9 10 L9.9 8.9 L12.5 9.6 L12.5 11.5 C12.5 12 12 12.5 11.5 12.5 C7.3 12.2 3.8 8.7 3.5 4.5 C3.5 4 4 3.5 4.5 3.5 Z"/>
        </svg>
        <span class="phone-number">724 555 01 48</span>
      </div>
      <p class="address">18635 Walden highway Brackton pa 15872</p>
    </div>
  </section>

  <section class="card card-front" aria-label="Brand side of the business card">
    <svg class="waves" viewBox="0 0 520 300" preserveAspectRatio="none" aria-hidden="true">
      <path fill="var(--wave-pale)" d="M0,162 C60,150 110,150 160,170 C220,192 250,222 320,230 C390,238 450,222 520,226 V300 H0 Z"/>
      <path fill="var(--wave-light)" opacity=".85" d="M0,176 C55,166 105,168 155,186 C215,208 245,236 315,242 C385,248 450,236 520,240 V300 H0 Z"/>
      <path fill="var(--wave-mid)" d="M0,188 C50,180 100,182 150,200 C210,222 240,250 310,256 C380,262 450,250 520,252 V300 H380 C330,300 280,290 240,280 C180,266 120,236 60,238 C35,238 15,242 0,246 Z"/>
      <path fill="var(--wave-deep)" d="M0,200 C45,194 95,196 145,214 C205,236 235,262 300,268 C370,274 445,262 520,264 V300 H330 C270,296 220,276 170,256 C110,234 50,236 0,240 Z"/>
    </svg>
    <div class="brand-lockup">
      <span class="brand-dot" aria-hidden="true"></span>
      <h1 class="brand-name">The Tide Parlor</h1>
    </div>
    <p class="website">Thetideparlor.example</p>
  </section>

</main>
</body>
</html>
```